Dental Business Card

We are looking for a double sided business card that can be easily customized with the names of the different members of our dental team.

I would like the background to be the 2-tone blue fleur-de-lis type pattern on the sides of our website (www.harborvalebrights.com).

I would like the logo attached incorporated.

I would like our address (2847 Birchmont Court, Suite 100, Alderbrook, VA 24410), phone number (555-318-4902), fax number (555-318-4977), website (www.harborvalebrights.com), and email address (info@harborvalebrights.com) all included on the front side.

Something a little more artistic to complement/highlight the logo on the back would be interesting.

I would like the business card to look professional, slightly feminine, and expense.

```html
<!DOCTYPE html>
<html lang="en">
<head>
<meta charset="utf-8">
<title>Harborvale Brights – Business Card</title>
<link rel="stylesheet" href="https://fonts.googleapis.com/css2?family=Cormorant+Garamond:wght@500;600&family=PT+Sans&display=swap">
<style>
  :root {
    --page: #ffffff;
    --label: #a7a9ac;
    --card-light: #c6dbeb;
    --card-mid: #aecbe2;
    --navy: #1a55a3;
    --brand: #1c5aa6;
    --sky: #3f86c8;
    --white: #ffffff;
    --serif: "Cormorant Garamond", Georgia, serif;
    --sans: "PT Sans", Arial, sans-serif;
  }
  * { margin: 0; padding: 0; box-sizing: border-box; }
  html, body { width: 1200px; height: 439px; overflow: hidden; background: var(--page); }
  .sheet { position: relative; width: 1200px; height: 439px; }

  .side-label {
    position: absolute; top: 32px; width: 200px; margin-left: -100px;
    text-align: center; font-family: var(--sans); font-size: 19px;
    color: var(--label); letter-spacing: 0.5px;
  }
  .side-label.front { left: 319px; }
  .side-label.back { left: 901px; }

  .card {
    position: absolute; top: 62px; width: 514px; height: 296px; overflow: hidden;
    font-variant-numeric: lining-nums;
  }
  .card.front { left: 62px; }
  .card.back { left: 644px; }
  .card-pattern {
    position: absolute; inset: 0;
    background: radial-gradient(ellipse at 50% 45%, var(--card-light) 0%, var(--card-mid) 100%);
  }

  .brand-mark {
    position: absolute; left: 50%; top: 74px; width: 50px; height: 50px; margin-left: -25px;
    border-radius: 50%; border: 2px solid var(--brand);
  }

  .brand-name {
    position: absolute; left: 0; right: 0; text-align: center; white-space: nowrap;
    font-family: var(--serif); font-weight: 600; font-variant: small-caps;
    color: var(--brand); letter-spacing: 0.5px; line-height: 1;
  }
  .front .brand-name { top: 132px; font-size: 36px; }
  .back .brand-name { top: 82px; font-size: 27px; }

  .tagline {
    position: absolute; top: 171px; left: 0; right: 0;
    display: flex; align-items: center; justify-content: center; gap: 8px;
    font-family: var(--serif); font-weight: 600; font-size: 14px; line-height: 18px;
    letter-spacing: 1.5px; color: var(--brand); white-space: nowrap;
  }
  .tagline .rule { width: 66px; height: 1px; background: var(--brand); }

  .address-band {
    position: absolute; top: 212px; left: 0; right: 0; height: 38px;
    background: var(--navy); color: var(--white);
    font-family: var(--serif); font-weight: 500; font-size: 20px;
    line-height: 38px; text-align: center; white-space: nowrap;
  }

  .contact {
    position: absolute; top: 258px; left: 0; right: 0;
    display: flex; justify-content: center; white-space: nowrap;
    font-family: var(--sans); font-size: 14.5px; line-height: 18px; color: var(--brand);
  }
  .contact-web { text-align: right; padding-right: 4px; border-right: 1px solid var(--brand); }
  .contact-phone { padding-left: 4px; }

  .person-name {
    position: absolute; top: 136px; left: 0; right: 0; text-align: center; line-height: 1;
    font-family: var(--serif); font-weight: 500; font-size: 36px; color: var(--navy);
    white-space: nowrap;
  }
  .person-name .surname { color: var(--sky); }
  .credential {
    position: absolute; top: 182px; left: 0; right: 0; text-align: center; line-height: 1;
    font-family: var(--serif); font-weight: 600; font-size: 17px; color: var(--navy);
  }
</style>
</head>
<body>
<main class="sheet">
  <div class="side-label front">FRONT</div>
  <div class="side-label back">BACK</div>

  <section class="card front">
    <div class="card-pattern" role="img" aria-label="Two-tone blue damask fleur-de-lis background pattern"></div>
    <div class="brand-mark"></div>
    <div class="brand-name">Harborvale Brights</div>
    <div class="tagline"><span class="rule"></span>REFINED DENTAL CARE<span class="rule"></span></div>
    <div class="address-band">2847 Birchmont Court, Suite 100, Alderbrook, VA 24410</div>
    <div class="contact">
      <div class="contact-web">info@harborvalebrights.com<br>www.harborvalebrights.com</div>
      <div class="contact-phone">Phone: 555-318-4902<br>Fax&nbsp;&nbsp;&nbsp;&nbsp;: 555-318-4977</div>
    </div>
  </section>

  <section class="card back">
    <div class="card-pattern" role="img" aria-label="Two-tone blue damask fleur-de-lis background pattern"></div>
    <div class="brand-name">Harborvale Brights</div>
    <div class="person-name">Dr. Elena R. <span class="surname">Whitford</span></div>
    <div class="credential">DMD</div>
  </section>
</main>
</body>
</html>
```